New Business Card Design Project

The look of the business cards should include
-Clean Lines
-Should suit a sophisticated customer
-Evoke a mix of business and creativity
-Incorporate the color Gray or Black:White palette
-Open to see layouts in both vertical and horizontal
3 partners (we need 3 cards)
DORENE VASK
ELKE TARNOWSKI
NENA QUASTIGO
Reason: We would like more submissions please
Target Market(s)
We are a NYC and European based boutique consulting agency specializing in fashion business and creative clients. In addition to consulting we will be offering an e-commerce site selling women’s accessories and jewelry geared towards fashion forward women ages 25-50.
Industry/Entity Type
Business
Requirements
Must have
- - texture
- grayscale
3 Partners
Details for each card
CONSULTING I DESIGN
NENA QUASTIGO
Founding Partner
646.208.3371
nenA@themarlowtidecollective.com
www.themarlowtidecollective.com
CONSULTING I DESIGN
DORENE VASK
Founding Partner
646.851.2907
dorene@themarlowtidecollective.com
www.themarlowtidecollective.com
CONSULTING I DESIGN
Elke Dunsford Tarnowski
Founding Partner
(no phone for her)
Elke@themarlowtidecollective.com
www.themarlowtidecollective.com

```html
<!DOCTYPE html>
<html lang="en">
<head>
<meta charset="utf-8">
<title>The Marlow Tide Collective — Business Cards</title>
<link rel="stylesheet" href="https://fonts.googleapis.com/css2?family=Nunito+Sans:wght@300;400;700&display=swap">
<style>
  :root {
    --canvas: #e4e3e1;
    --card-white: #f7f7f6;
    --panel-gray: #666666;
    --ink: #3a3a3a;
    --ink-on-gray: #f2f2f2;
    --ink-soft-on-gray: #d9d9d9;
    --shadow: rgba(0, 0, 0, 0.18);
  }
  * { margin: 0; padding: 0; box-sizing: border-box; }
  html, body {
    width: 1200px;
    height: 1000px;
    overflow: hidden;
    background: var(--canvas);
    font-family: "Nunito Sans", sans-serif;
  }
  .sheet {
    position: relative;
    width: 1200px;
    height: 1000px;
  }
  .card {
    position: absolute;
    left: 250px;
    width: 700px;
    height: 400px;
    background: var(--card-white);
    box-shadow: 0 14px 30px var(--shadow), 0 2px 4px var(--shadow);
    overflow: hidden;
  }
  .card--front { top: 80px; }
  .card--back  { top: 520px; display: flex; }

  /* Wordmark */
  .wordmark {
    display: flex;
    align-items: center;
    gap: 18px;
    color: var(--ink);
  }
  .wordmark__square {
    width: 22px;
    height: 22px;
    border: 2px solid var(--ink);
    flex: none;
  }
  .wordmark__name {
    font-weight: 400;
    font-size: 30px;
    line-height: 1.15;
    letter-spacing: 0.28em;
    text-transform: uppercase;
  }
  .card--front .wordmark {
    position: absolute;
    inset: 0;
    justify-content: center;
  }
  .card--back .wordmark { gap: 12px; }
  .card--back .wordmark__square { width: 14px; height: 14px; border-width: 1.5px; }
  .card--back .wordmark__name { font-size: 19px; letter-spacing: 0.22em; }

  .card__logo-side {
    width: 45%;
    display: flex;
    align-items: center;
    justify-content: center;
  }
  .card__info-panel {
    width: 55%;
    background: var(--panel-gray);
    color: var(--ink-on-gray);
    padding: 70px 30px 0 44px;
  }
  .info__tagline {
    font-weight: 300;
    font-size: 15px;
    letter-spacing: 0.06em;
    color: var(--ink-soft-on-gray);
    margin-bottom: 16px;
  }
  .info__name {
    font-weight: 700;
    font-size: 20px;
    letter-spacing: 0.04em;
    margin-bottom: 4px;
  }
  .info__line {
    font-weight: 300;
    font-size: 15px;
    line-height: 1.5;
    color: var(--ink-soft-on-gray);
  }
  .info__web { margin-top: 22px; }
</style>
</head>
<body>
<main class="sheet">
  <section class="card card--front" aria-label="Card front">
    <div class="wordmark">
      <span class="wordmark__square"></span>
      <span class="wordmark__name">The<br>Marlow<br>Tide<br>Collective</span>
    </div>
  </section>

  <section class="card card--back" aria-label="Card back">
    <div class="card__logo-side">
      <div class="wordmark">
        <span class="wordmark__square"></span>
        <span class="wordmark__name">The<br>Marlow<br>Tide<br>Collective</span>
      </div>
    </div>
    <div class="card__info-panel">
      <p class="info__tagline">CONSULTING I DESIGN</p>
      <p class="info__name">NENA QUASTIGO</p>
      <p class="info__line">Founding Partner</p>
      <p class="info__line">646.208.3371</p>
      <p class="info__line">nenA@themarlowtidecollective.com</p>
      <p class="info__line info__web">www.themarlowtidecollective.com</p>
    </div>
  </section>
</main>
</body>
</html>
```